Postcard Design Project( EDDM 6.5in wide x 9in )

Painting Company
- Interior and Exterior Painting
- Wallpaper Removal and Installation
- Wood Staining
-Licensed and Insured HIC #PA739408
-website: www.miloverhunpainting.com
-Facebook: @verhpainting
-Phone #: 555-218-3064
Fall Special Discount 10% off $500.00 or more
(EDDM Postcard size (6.5in wide x9)

Target Market(s)

People who are in need of painting

Industry/Entity Type

Painting

Requirements
Must have
• Must be bold and make a statement. I need the people to hold on to the postcard and not throw it away.
Should not have
• Should not look like you took it off a template.

```html
<!DOCTYPE html>
<html lang="en">
<head>
<meta charset="utf-8">
<title>Milo Verhun Painting – EDDM Postcard</title>
<link rel="stylesheet" href="https://fonts.googleapis.com/css2?family=Rubik+Dirt&family=Oswald:wght@600&family=Cormorant+Garamond:wght@500&family=Arimo:wght@400&display=swap">
<style>
  :root {
    --ink: #0b0b0b;
    --paper: #ffffff;
    --page: #ffffff;
    --rule: #a9a9a9;
    --stamp: #c6c6c6;
    --muted: #2a2a2a;
    --brick: #1c1c1c;
  }
  * { margin: 0; padding: 0; box-sizing: border-box; }
  html, body { width: 900px; height: 1200px; overflow: hidden; background: var(--page); }
  .canvas { position: relative; width: 900px; height: 1200px; font-family: "Arimo", Arial, sans-serif; color: var(--ink); }

  .card {
    position: absolute; left: 99px; width: 708px; height: 477px;
    background: var(--paper); overflow: hidden;
    box-shadow: 2px 3px 6px rgba(0,0,0,.35);
  }
  .card--front { top: 53px; }
  .card--back { top: 612px; height: 478px; }
  .side-label {
    position: absolute; left: 0; width: 900px; text-align: center;
    font-family: "Arimo", Arial, sans-serif; font-size: 36px; color: #111;
  }
  .side-label--front { top: 553px; }
  .side-label--back { top: 1103px; }

  .layer { position: absolute; left: 0; top: 0; }

  /* front */
  .brand {
    position: absolute; left: 70px; top: 36px; width: 200px; text-align: right;
    font-family: "Cormorant Garamond", Georgia, serif; font-weight: 500;
    font-size: 27px; line-height: 30px; color: #3a3a3a;
  }
  .stars { position: absolute; left: 260px; top: 0; width: 140px; height: 170px;
    background: radial-gradient(ellipse at 70% 30%, rgba(0,0,0,.14), rgba(0,0,0,0) 70%); }
  .headline { position: absolute; left: 32px; top: 122px; }
  .intro {
    position: absolute; left: 38px; top: 260px; width: 276px;
    font-size: 9.6px; line-height: 12.6px; text-align: justify; color: var(--muted);
  }
  .thumb { position: absolute; top: 330px; width: 126px; height: 99px;
    border: 3px solid var(--ink); border-radius: 4px; }
  .thumb--exterior { left: 41px; background: linear-gradient(180deg,#9cc4e4 0%,#e9e4cc 45%,#5b7040 100%); }
  .thumb--interior { left: 187px; background: linear-gradient(180deg,#cfc6b6 0%,#efe9df 55%,#6a5548 100%); }
  .portrait { position: absolute; left: 395px; top: 48px; width: 313px; height: 429px;
    background: linear-gradient(180deg,#3b3f4d 0%,#6b85ad 35%,#1f2b48 75%,#e9e9e9 100%);
    border-radius: 140px 140px 0 0; }

  /* back */
  .services { position: absolute; left: 20px; top: 307px; list-style: none; font-size: 10.5px; line-height: 13px; }
  .services li { position: relative; padding-left: 13px; margin-bottom: 8px; width: 150px; }
  .services li::before { content: ""; position: absolute; left: 0; top: 3px; width: 7px; height: 7px; border-radius: 50%; background: var(--ink); }
  .divider { position: absolute; left: 176px; top: 303px; width: 1.5px; height: 106px; background: var(--ink); }
  .offer { position: absolute; left: 186px; top: 306px; width: 140px; text-align: center; }
  .offer__small { font-size: 8.6px; line-height: 11px; }
  .offer__small--hic { margin-top: 0; }
  .phone { position: absolute; left: 28px; top: 451px; font-size: 11px; color: var(--paper); }
  .stamp { position: absolute; left: 557px; top: 38px; width: 82px; height: 92px; background: var(--stamp); }
  .address-line { position: absolute; left: 470px; width: 193px; height: 3px; background: var(--rule); }
</style>
</head>
<body>
<div class="canvas">

  <section class="card card--front">
    <div class="stars" role="img" aria-label="Faint star field decoration"></div>

    <svg class="layer" width="708" height="477" viewBox="0 0 708 477" aria-hidden="true">
      <path d="M372 0 H708 V440 C690 430 676 420 668 400 L600 470 H470 C430 440 400 410 395 360
               C380 300 385 250 372 200 C360 150 350 90 372 0 Z" fill="var(--brick)"/>
      <path d="M0 458 C60 448 120 452 200 446 C280 441 360 450 460 452 L470 470 L0 477 Z" fill="var(--ink)"/>
    </svg>

    <div class="portrait" role="img" aria-label="Photo of a smiling painter in cap, checked shirt and overalls holding a paint roller"></div>

    <p class="brand">Milo Verhun<br>Painting</p>

    <svg class="headline" width="290" height="130" viewBox="0 0 290 130">
      <text x="2" y="66" textLength="278" lengthAdjust="spacingAndGlyphs"
            font-family="'Rubik Dirt', Impact, sans-serif" font-size="80" fill="var(--ink)">VETERAN</text>
      <text x="5" y="89" textLength="276" lengthAdjust="spacingAndGlyphs"
            font-family="Oswald, 'Arial Narrow', sans-serif" font-weight="600" font-size="17" fill="var(--ink)">OWNED BUSINESSWITH EXPERIENCE</text>
      <text x="5" y="108" textLength="276" lengthAdjust="spacing"
            font-family="Oswald, 'Arial Narrow', sans-serif" font-weight="600" font-size="11.5" fill="var(--ink)">OF PROVIDING QUALITY WORK</text>
      <path d="M6 121 H282" stroke="var(--ink)" stroke-width="1.6"/>
    </svg>

    <p class="intro">Milo Verhun Painting will apply 1 to 2 coats of paint on all surfaces. We use Hartwell Coatings Paint, unless otherwise directed by the customer. With quality products of Velour (Interior), Duraflex (Interior/Exterior), and Weatherguard (Exterior), you're sure to get a smooth finish.</p>

    <div class="thumb thumb--exterior" role="img" aria-label="Photo of a freshly painted two-storey house exterior"></div>
    <div class="thumb thumb--interior" role="img" aria-label="Photo of a freshly painted interior room"></div>
  </section>
  <p class="side-label side-label--front">front</p>

  <section class="card card--back">
    <svg class="layer" width="708" height="478" viewBox="0 0 708 478">
      <defs>
        <linearGradient id="houseScene" x1="0" y1="0" x2="0" y2="1">
          <stop offset="0" stop-color="#7fb3e6"/>
          <stop offset="0.35" stop-color="#c9c3b4"/>
          <stop offset="0.65" stop-color="#8a8a80"/>
          <stop offset="0.8" stop-color="#2f3340"/>
          <stop offset="1" stop-color="#3f3f48"/>
        </linearGradient>
        <radialGradient id="starFade" cx="0.3" cy="0.5" r="0.7">
          <stop offset="0" stop-color="#000" stop-opacity=".14"/>
          <stop offset="1" stop-color="#000" stop-opacity="0"/>
        </radialGradient>
      </defs>
      <rect x="0" y="215" width="110" height="100" fill="url(#starFade)" role="img" aria-label="Faint star field decoration"/>
      <path role="img" aria-label="Photo of a large house with a double garage and freshly sealed driveway"
            d="M0 0 H340 C345 30 360 60 380 90 C390 120 370 150 350 180 C340 205 330 215 310 225
               C250 248 150 250 60 245 C30 240 10 230 0 220 Z" fill="url(#houseScene)"/>
      <path d="M318 212 C392 250 395 390 350 472" fill="none" stroke="var(--ink)" stroke-width="6" stroke-linecap="round"/>
      <path d="M0 418 C40 410 90 416 150 412 C220 408 300 414 372 410 L395 474 L0 478 Z" fill="var(--ink)"/>
    </svg>

    <ul class="services">
      <li>Interior and Exterior Painting</li>
      <li>Wood Staining</li>
      <li>Wallpaper Removal and Installation</li>
    </ul>
    <div class="divider"></div>

    <div class="offer">
      <svg width="140" height="28" viewBox="0 0 140 28">
        <text x="2" y="24" textLength="134" lengthAdjust="spacingAndGlyphs"
              font-family="'Rubik Dirt', Impact, sans-serif" font-size="24" fill="var(--ink)">10% Discount</text>
      </svg>
      <p class="offer__small">Fall Special&nbsp; off $500.00 or more</p>
      <svg width="140" height="30" viewBox="0 0 140 30">
        <text x="6" y="26" textLength="128" lengthAdjust="spacingAndGlyphs"
              font-family="'Rubik Dirt', Impact, sans-serif" font-size="22" fill="var(--ink)">HIC #PA739408</text>
      </svg>
      <p class="offer__small offer__small--hic">Licensed and Insured</p>
    </div>

    <p class="phone">Phone #: 555-218-3064</p>

    <div class="stamp"></div>
    <div class="address-line" style="top:245px"></div>
    <div class="address-line" style="top:294px"></div>
    <div class="address-line" style="top:344px"></div>
  </section>
  <p class="side-label side-label--back">back</p>

</div>
</body>
</html>
```